Box and label design for oil Tincture bottle

I need to design an attractive looking label for a 30ml CBD oil tincture along with designing a box for the tincture oil. I already have the logo (see attachment). I just need a nice, attractive looking artwork for the label and the box. The box is the standard 30ml tincture oil (see example attachment). The box has a total of 6 sides (4 on sides and 2 for top and bottom). Please include a section for supplemental facts and ingredients. Let's not focus to much on content. I am more concerned with design of box and label.
Target Market(s)
CBD customers
Look and feel
Each slider illustrates characteristics of the customer's brand and the style your logo design should communicate.

```html
<!DOCTYPE html>
<html lang="en">
<head>
<meta charset="utf-8">
<title>Clear Meadow CBD – 30 ml Tincture Label</title>
<link href="https://fonts.googleapis.com/css2?family=Jost:wght@600;700;800&display=swap" rel="stylesheet">
<style>
  :root {
    --brand-blue: #0a92d0;
    --deep-blue: #0553a4;
    --navy: #1d3c8f;
    --panel-tint: #d1e8f5;
    --text-blue: #1a8fd0;
    --white: #ffffff;
  }
  * { margin: 0; padding: 0; box-sizing: border-box; }
  html, body { width: 1200px; height: 600px; overflow: hidden; background: var(--white); }
  .label {
    position: relative;
    width: 1200px;
    height: 600px;
    font-family: "Jost", "Futura", sans-serif;
    background: var(--white);
    overflow: hidden;
  }
  .top-band {
    position: absolute; left: 0; top: 0; width: 100%; height: 30px;
    background: linear-gradient(90deg, var(--brand-blue), #0b8fcc);
  }
  .bottom-band {
    position: absolute; left: 0; top: 438px; width: 100%; height: 162px;
    background: linear-gradient(90deg, var(--deep-blue) 0%, #0a7cc4 60%, var(--brand-blue) 100%);
  }
  .info-panel {
    position: absolute; top: 106px; width: 177px; height: 278px;
    background: var(--panel-tint); border-radius: 8px;
    padding: 17px 4px 0 7px; color: var(--text-blue);
  }
  .info-panel--directions { left: 20px; }
  .info-panel--ingredients { left: 1004px; padding-left: 8px; }
  .info-panel__title {
    font-size: 15px; font-weight: 800; text-decoration: underline;
    text-underline-offset: 3px; margin: 0 0 9px 6px; letter-spacing: 0.2px;
  }
  .info-panel--ingredients .info-panel__title { margin-left: 11px; }
  .info-panel__body {
    font-size: 11px; font-weight: 700; line-height: 15.2px; white-space: nowrap;
  }
  .brand-panel {
    position: absolute; left: 409px; top: 88px; width: 383px; height: 382px;
    background: var(--panel-tint); border-radius: 8px;
    display: flex; flex-direction: column; align-items: center;
  }
  .brand-panel__mark {
    width: 150px; height: 150px; border-radius: 50%;
    background: var(--navy); margin-top: 70px;
  }
  .brand-panel__name {
    margin-top: 46px; text-align: center; white-space: nowrap;
    color: var(--navy); font-weight: 800; font-size: 39px; line-height: 42px;
    letter-spacing: 0.3px;
  }
  .tagline {
    position: absolute; left: 0; top: 482px; width: 100%;
    text-align: center; color: var(--panel-tint); white-space: nowrap;
    font-size: 57px; font-weight: 800; letter-spacing: 0; line-height: 80px;
  }
  .volume-tab {
    position: absolute; left: 556px; top: 568px; width: 88px; height: 40px;
    background: var(--panel-tint); border-radius: 8px;
    text-align: center; color: var(--text-blue);
    font-size: 15px; font-weight: 800; padding-top: 3px;
    text-decoration: underline; text-underline-offset: 3px;
  }
</style>
</head>
<body>
<main class="label">
  <div class="top-band"></div>
  <div class="bottom-band"></div>

  <section class="info-panel info-panel--directions">
    <h2 class="info-panel__title">DIRECTIONS:</h2>
    <p class="info-panel__body">Lorem ipsum dolor sit amet,<br>consectetur adipiscing elit,<br>sed do eiusmod tempor inci<br>didunt ut labore et dolorema<br>gna aliqua. Ut enim ad mini<br>m veniam, quis nostrud exer<br>citation ullamco laboris nisi<br>ut aliquip ex ea commodoco<br>nsequat. Duis aute irure dol.</p>
  </section>

  <section class="brand-panel">
    <div class="brand-panel__mark"></div>
    <h1 class="brand-panel__name">CLEAR MEADOW<br>CBD</h1>
  </section>

  <section class="info-panel info-panel--ingredients">
    <h2 class="info-panel__title">INGREDIENTS:</h2>
    <p class="info-panel__body">Lorem ipsum dolor sit amet,<br>consectetur adipiscing elit,<br>sed do eiusmod tempor inci<br>didunt ut labore et dolorema<br>gna aliqua. Ut enim ad mini<br>m veniam, quis nostrud exer<br>citation ullamco laboris nisi<br>ut aliquip ex ea commodoco<br>nsequat. Duis aute irure dol.</p>
  </section>

  <p class="tagline">100% NATURAL CANNABIS TINCTURE</p>
  <div class="volume-tab">30 ml</div>
</main>
</body>
</html>
```